Business cards and stationary for training company
Company in Japan specializing in corporate training
Business cards and stationary for training company  - Corporate Services
Creative Brief
Use specific fonts
Please help with this
Professional
Brandon Mallory
President
4-17-3 Hoshimidai, Adachi, Tokyo 123-0845
brandon@brightpathlearninggroup.example
BrightPathLearningGroup.example
Will update information soon
I'm thinking to use one side for logo and other for contact info, however I need English and Japanese writing
Concepts
Business Cards and Stationery for new compliance company.
Business Cards and Stationery for Background Check Company
Leftnut Leftnut
Thank you everyone for the great designs. I will be using the stationary for rinted material and would need to think printer friendly. Thus, would it be possible to see letter head with a simple design that will look good in a thirty page booklet? Thank you.
Great so far, however it would great to see some stationary

```html
<!DOCTYPE html>
<html lang="en">
<head>
<meta charset="utf-8">
<title>BrightPath Stationery Set</title>
<link href="https://fonts.googleapis.com/css2?family=Roboto:wght@400;700&display=swap" rel="stylesheet">
<style>
  :root{
    --bg:#9c9fa3;
    --paper:#ffffff;
    --brand:#1f5aa6;
    --band-grey:#c9cbcd;
    --ink:#5d6166;
    --label:#e6e7e8;
    --line:#d4d6d8;
  }
  *{box-sizing:border-box;margin:0;padding:0}
  html,body{width:1200px;height:490px;overflow:hidden}
  body{
    background:radial-gradient(ellipse at 50% 45%, #b3b6b9 0%, var(--bg) 75%);
    font-family:"Roboto", Arial, sans-serif;
    position:relative;
  }
  .item{position:absolute}
  .sheet{background:var(--paper);box-shadow:0 2px 6px rgba(0,0,0,.25)}
  .label{position:absolute;font-size:6px;color:var(--label);white-space:nowrap;transform:translate(-50%,-10px);left:50%;top:0}
  .logo{position:absolute;display:flex;align-items:center;gap:3px;color:var(--brand);font-weight:700;letter-spacing:.5px;white-space:nowrap}
  .logo .mark{display:block;background:var(--brand)}
  .logo.flip{transform:rotate(180deg)}
  .band{position:absolute;left:0;right:0;bottom:6px;height:5px;
    background:linear-gradient(100deg,var(--brand) 0 62%,var(--band-grey) 62% 100%)}
  .small-text{font-size:4px;line-height:6px;color:var(--ink)}

  /* folder */
  .folder{left:24px;top:67px;width:456px;height:379px}
  .folder svg{position:absolute;inset:0;filter:drop-shadow(0 2px 4px rgba(0,0,0,.25))}

  /* cd */
  .cd{left:516px;top:67px;width:82px;height:82px}
  .cd .disc{width:82px;height:82px;border-radius:50%;background:var(--paper);box-shadow:0 2px 6px rgba(0,0,0,.25);position:relative}
  .cd .hole{position:absolute;left:32px;top:32px;width:18px;height:18px;border-radius:50%;background:var(--bg);box-shadow:0 0 0 4px #eceded}

  .sleeve{left:619px;top:34px;width:101px;height:146px}
  .sleeve .cut{position:absolute;right:-14px;top:58px;width:28px;height:28px;border-radius:50%;background:var(--bg)}

  .card{width:86px;height:53px;top:96px}
  .card.front{left:737px}
  .card.back{left:832px}
  .slip{left:936px;top:96px;width:134px;height:58px}

  .letter{top:168px;width:197px;height:278px}
  .letter.form{left:499px}
  .letter.plain{left:715px}
  .contact{position:absolute;right:14px;top:40px;text-align:left}
  .order-table{position:absolute;left:14px;top:60px;width:120px;border-collapse:collapse}
  .order-table td{border:.6px solid var(--line);height:9px}
  .order-table td.head{background:#eef0f2}
  .options{position:absolute;left:14px;top:178px;display:flex;gap:9px}
  .options span{display:flex;align-items:center;gap:2px}
  .options i{display:block;width:4px;height:4px;border:.6px solid var(--ink)}

  .envelope{left:931px;width:139px;height:96px}
  .envelope.front{top:211px}
  .envelope.back{top:332px;height:108px}
  .envelope.back svg{position:absolute;inset:0}
</style>
</head>
<body>

  <!-- Folder -->
  <div class="item folder">
    <span class="label">Folder</span>
    <svg width="456" height="379" viewBox="0 0 456 379">
      <path d="M0 0 H456 V255 H0 Z" fill="#fff"/>
      <path d="M0 255 H212 V330 Q212 379 170 379 H30 Q0 379 0 350 Z" fill="#fff"/>
      <path d="M232 255 H456 V350 Q456 379 426 379 H278 Q232 379 232 330 Z" fill="#fff"/>
      <path d="M0 240 H456 V246 H0 Z" fill="#1f5aa6"/>
      <path d="M300 240 H456 V246 H300 Z" fill="#c9cbcd"/>
    </svg>
    <div class="logo" style="left:250px;top:48px;font-size:14px"><span class="mark" style="width:9px;height:9px"></span>BRIGHTPATH</div>
    <div class="logo" style="left:30px;top:128px;font-size:17px"><span class="mark" style="width:11px;height:11px"></span>BRIGHTPATH</div>
    <div class="logo flip" style="left:40px;top:336px;font-size:11px"><span class="mark" style="width:7px;height:7px"></span>BRIGHTPATH</div>
    <div class="logo flip" style="left:275px;top:336px;font-size:11px"><span class="mark" style="width:7px;height:7px"></span>BRIGHTPATH</div>
  </div>

  <!-- CD -->
  <div class="item cd">
    <span class="label">CD</span>
    <div class="disc"><div class="hole"></div>
      <div class="logo" style="left:16px;top:18px;font-size:5px"><span class="mark" style="width:3px;height:3px"></span>BRIGHTPATH</div>
    </div>
  </div>

  <div class="item sheet sleeve">
    <span class="label">CD Sleeve</span>
    <div class="cut"></div>
    <div class="logo" style="left:10px;top:22px;font-size:7px"><span class="mark" style="width:5px;height:5px"></span>BRIGHTPATH</div>
    <div class="band"></div>
  </div>

  <!-- Business cards -->
  <div class="item sheet card front">
    <span class="label">Business Card Front</span>
    <div class="logo" style="left:12px;top:18px;font-size:9px"><span class="mark" style="width:6px;height:6px"></span>BRIGHTPATH</div>
    <div class="band" style="bottom:4px;height:3px"></div>
  </div>
  <div class="item sheet card back">
    <span class="label">Business Card Back</span>
    <div class="logo" style="left:6px;top:6px;font-size:5px"><span class="mark" style="width:3px;height:3px"></span>BRIGHTPATH</div>
    <div class="small-text" style="position:absolute;left:6px;top:16px;font-size:3px;line-height:4px">
      Brandon Mallory<br>4-17-3 Hoshimidai, Adachi, Tokyo 123-0845<br>brandon@brightpathlearninggroup.example<br>BrightPathLearningGroup.example
    </div>
    <div class="band" style="bottom:4px;height:3px"></div>
  </div>

  <div class="item sheet slip">
    <span class="label">Compliment Slip</span>
    <div class="logo" style="left:10px;top:12px;font-size:9px"><span class="mark" style="width:6px;height:6px"></span>BRIGHTPATH</div>
    <div class="band" style="bottom:5px;height:3px"></div>
  </div>

  <!-- Letterheads -->
  <div class="item sheet letter form">
    <span class="label">Order Form</span>
    <div class="logo" style="left:14px;top:16px;font-size:13px"><span class="mark" style="width:8px;height:8px"></span>BRIGHTPATH</div>
    <div class="contact small-text">4-17-3 Hoshimidai<br>Adachi, Tokyo 123-0845<br>BrightPathLearningGroup.example</div>
    <table class="order-table">
      <tr><td class="head"></td><td class="head"></td><td class="head"></td></tr>
      <tr><td></td><td></td><td></td></tr>
      <tr><td></td><td></td><td></td></tr>
      <tr><td></td><td></td><td></td></tr>
      <tr><td></td><td></td><td></td></tr>
      <tr><td></td><td></td><td></td></tr>
      <tr><td></td><td></td><td></td></tr>
    </table>
    <div class="options small-text">
      <span><i></i>Option</span><span><i></i>Option</span><span><i></i>Option</span><span><i></i>Option</span><span><i></i>Option</span>
    </div>
    <div class="band"></div>
  </div>

  <div class="item sheet letter plain">
    <span class="label">Letterhead</span>
    <div class="logo" style="left:14px;top:16px;font-size:13px"><span class="mark" style="width:8px;height:8px"></span>BRIGHTPATH</div>
    <div class="contact small-text">4-17-3 Hoshimidai<br>Adachi, Tokyo 123-0845<br>brandon@brightpathlearninggroup.example<br>BrightPathLearningGroup.example</div>
    <div class="band"></div>
  </div>

  <!-- Envelopes -->
  <div class="item sheet envelope front">
    <span class="label">Envelope Front</span>
    <div class="logo" style="left:10px;top:10px;font-size:10px"><span class="mark" style="width:6px;height:6px"></span>BRIGHTPATH</div>
    <div class="band" style="bottom:5px;height:4px"></div>
  </div>
  <div class="item sheet envelope back">
    <span class="label">Envelope Back</span>
    <svg width="139" height="108" viewBox="0 0 139 108">
      <path d="M0 0 L69.5 58 L139 0" fill="none" stroke="#c9cbcd" stroke-width="1"/>
      <path d="M0 108 L52 46 M139 108 L87 46" fill="none" stroke="#e2e3e4" stroke-width="1"/>
    </svg>
    <div class="band" style="bottom:5px;height:4px"></div>
  </div>

</body>
</html>
```